Cobalt Ridge

Build a simple scrollable "floating" website - Website should have polished, modern look.
Domain has been bought on NestRoster and website should be setup there.
Project Brief:
https://slides.quorvane.com/deck/7Kp2Xa9Lm4Qe8Rt1Vb6Nc3Hz5Wy0Jd/edit?share=open
Input Files:
https://www.filtravo.com/f/k3mp81zt07qvr5n/BBDXnaQGyTsC_prLJFHK8u3xb?get=0

Build

```html
<!DOCTYPE html>
<html lang="en">
<head>
<meta charset="utf-8">
<title>Tidemark Circuit</title>
<link rel="stylesheet" href="https://fonts.googleapis.com/css2?family=Raleway:wght@500;600;700&family=Open+Sans:wght@400;600;700&display=swap">
<style>
:root{
  --red:#b9300d;
  --teal:#1b5c69;
  --ink:#1e1e1e;
  --body:#6b6b6b;
  --grey-band:#f4f4f4;
  --line:#dadada;
  --footer:#17191b;
  --white:#ffffff;
}
*{box-sizing:border-box;margin:0;padding:0}
html,body{width:1200px;height:3109px;overflow:hidden}
body{position:relative;background:var(--white);font-family:"Open Sans",Arial,sans-serif;color:var(--body)}
section,header,footer{position:absolute;left:0;width:1200px}
.abs{position:absolute}
h2{font-family:"Raleway",Helvetica,sans-serif;font-weight:700;color:var(--ink);font-size:30px;letter-spacing:.3px}
.center{text-align:center;left:0;width:1200px}
.btn-outline{display:flex;align-items:center;justify-content:center;border:2px solid #cfcfcf;border-radius:30px;color:var(--red);font-family:"Open Sans",Arial,sans-serif;font-weight:700;font-size:14px;letter-spacing:.4px;background:var(--white)}
.btn-red{display:flex;align-items:center;justify-content:center;background:var(--red);color:var(--white);border-radius:24px;font-weight:700;font-size:13px;letter-spacing:.4px}

/* hero */
.hero{top:0;height:543px;background:linear-gradient(180deg,#3e5a7c 0%,#56749a 35%,#2f4a68 62%,#1d2f44 80%,#2b4a67 100%)}
.brand{left:100px;top:25px;display:flex;align-items:center;gap:12px}
.brand-mark{width:40px;height:40px;border-radius:50%;background:var(--teal);border:3px solid var(--white)}
.brand-name{font-family:"Raleway",Helvetica,sans-serif;font-weight:700;color:var(--white);font-size:20px;line-height:1.1;width:120px}
.nav{right:96px;top:64px;display:flex;gap:38px;align-items:center}
.nav a{color:var(--white);text-decoration:none;font-family:"Raleway",Helvetica,sans-serif;font-weight:600;font-size:15px;letter-spacing:.3px}
.hero-text{top:222px;color:var(--white);font-family:"Raleway",Helvetica,sans-serif;font-weight:600;font-size:27px;line-height:42px;text-shadow:0 1px 3px rgba(0,0,0,.4)}
.dots{top:489px;left:574px;display:flex;gap:4px}
.dots span{width:11px;height:11px;border-radius:50%;border:2px solid var(--white)}
.dots span.on{background:var(--white)}

/* trash sites */
.trash{top:543px;height:526px}
.trash h2{left:97px;top:97px}
.trash p{left:97px;width:490px;font-size:13.5px;line-height:23px}
.photo-frame{left:642px;top:74px;width:460px;height:370px;border:1px solid #ddd;padding:6px;background:var(--white);box-shadow:0 1px 4px rgba(0,0,0,.12)}
.photo-fill{width:100%;height:100%}

/* data */
.data{top:1069px;height:487px;background:var(--grey-band)}
.data h2{top:54px}
.card{top:129px;width:315px;height:257px;background:var(--white);border:1px solid var(--line);text-align:center}
.card svg{position:absolute;left:50%;top:20px;transform:translateX(-50%)}
.card h3{position:absolute;top:102px;left:10px;right:10px;font-family:"Open Sans",Arial,sans-serif;font-weight:600;color:var(--ink);font-size:15.5px;line-height:22px}
.card p{position:absolute;left:40px;right:40px;font-size:13.5px;line-height:23px}
.card .btn-red{position:absolute;left:90px;width:135px;height:40px;bottom:-21px}

/* expedition */
.expedition{top:1556px;height:997px}
.expedition h2{top:68px}
.expedition .lead{top:126px;left:180px;width:840px;font-size:13.5px;line-height:24px}
.video{left:331px;top:211px;width:537px;height:330px;border:1px solid #ddd;padding:5px;background:var(--white)}
.divider{left:97px;top:698px;width:1005px;height:1px;background:var(--line)}
.expedition .sponsors-title{top:754px}
.sponsor{top:821px;width:177px;height:103px;border:1px solid var(--line);display:flex;align-items:center;justify-content:center;font-family:"Raleway",Helvetica,sans-serif;font-weight:600;color:var(--ink);font-size:17px;background:var(--white)}
.sponsor .mark{width:18px;height:18px;border-radius:50%;background:var(--teal);margin-right:8px}

/* footer */
.footer{top:2553px;height:556px;background:linear-gradient(180deg,#1e2123 0%,var(--footer) 60%,#202426 100%);color:#d8d8d8}
.to-top{left:565px;top:25px;text-align:center;width:70px;color:var(--white);font-weight:700;font-size:12px}
.footer h4{font-family:"Raleway",Helvetica,sans-serif;font-weight:700;color:var(--white);font-size:20px;letter-spacing:.3px}
.field{background:var(--white);color:#888;font-size:11px;padding:8px 14px;height:31px}
.info-row{left:779px;display:flex;align-items:center;gap:24px;font-size:12.5px;color:#e4e4e4}
.info-icon{width:34px;height:34px;border-radius:50%;border:1px solid #666;display:flex;align-items:center;justify-content:center}
.social{width:30px;height:30px;border-radius:50%}
.foot-line{left:97px;top:472px;width:1005px;height:1px;background:#3a3d40}
.copyright{top:509px;font-size:12px;color:#cfcfcf}
</style>
</head>
<body>

<header class="hero" role="img" aria-label="Harbour skyline at dusk with city towers reflected on water">
  <div class="abs brand"><span class="brand-mark"></span><span class="brand-name">Tidemark Circuit</span></div>
  <nav class="abs nav">
    <a href="#">TRASH SITES</a><a href="#">RAW DATA</a><a href="#">EXPEDITION</a><a href="#">SUPPORTERS</a><a href="#">GET IN TOUCH</a>
    <svg width="16" height="16" viewBox="0 0 16 16"><circle cx="6.5" cy="6.5" r="4.8" fill="none" stroke="#fff" stroke-width="2"/><line x1="10" y1="10" x2="14.5" y2="14.5" stroke="#fff" stroke-width="2.2" stroke-linecap="round"/></svg>
  </nav>
  <p class="abs center hero-text">Results of the first ever water quality and pollution recording<br>of Hong Kong Islands 80 kilometer coastline. The data was recorded<br>during the 2017 Tidemark Circuit Expedition.</p>
  <div class="abs dots"><span class="on"></span><span></span><span></span><span></span></div>
</header>

<section class="trash">
  <h2 class="abs">HONG KONG ISLAND TRASH SITES</h2>
  <p class="abs" style="top:158px">Nemo enim ipsam voluptatem quia voluptas sit aspernatur aut odit aut fugit, sed quia consequuntur magni dolores eos qu.</p>
  <p class="abs" style="top:234px">Ratione voluptatem sequi nesciunt. Neque porro quisquam est, qui dolorem ipsum quia dolor sit amet, conse. Neque porro quisquam est, qui dolorem ip sum quia dolor sit amet, consectetur, adipisci velit, sed quia non numquamei us modi tempora incidunt ut labore et dolor.</p>
  <a class="abs btn-outline" style="left:97px;top:369px;width:131px;height:46px">READ MORE</a>
  <div class="abs photo-frame"><div class="photo-fill" role="img" aria-label="Discarded foam box washed up on a rocky shoreline" style="background:linear-gradient(160deg,#7d8a80 0%,#5b5f57 45%,#8a8378 70%,#4d4a44 100%)"></div></div>
</section>

<section class="data">
  <h2 class="abs center">DATA &amp; RESEARCH</h2>
  <div class="abs card" style="left:97px">
    <svg width="40" height="56" viewBox="0 0 40 56"><path d="M20 4 C20 4 4 26 4 38 a16 16 0 0 0 32 0 C36 26 20 4 20 4Z" fill="var(--teal)"/><path d="M12 38 a8 8 0 0 0 8 8" stroke="#fff" stroke-width="3" fill="none"/></svg>
    <h3>WATER POLLUTION</h3>
    <p style="top:136px">Nemo enim ipsam voluptatem quia voluptas sit aspernatur aut odit autfu git, sed quia consequun tur</p>
    <span class="btn-red">DOWNLOAD</span>
  </div>
  <div class="abs card" style="left:443px">
    <svg width="60" height="60" viewBox="0 0 60 60"><path d="M21 4h18v4h-3v16l17 28a4 4 0 0 1-3.5 6h-39A4 4 0 0 1 7 52l17-28V8h-3z" fill="var(--teal)"/><path d="M17 40h26l6 10H11z" fill="#fff" opacity=".35"/></svg>
    <h3>BIOCHEMISTRY DATA</h3>
    <p style="top:136px">Nemo enim ipsam voluptatem quia voluptas sit aspernatur aut odit autfu git, sed quia consequun tur</p>
    <span class="btn-red">DOWNLOAD</span>
  </div>
  <div class="abs card" style="left:787px">
    <svg width="50" height="66" viewBox="0 0 50 66"><path d="M2 2h32l14 14v48H2z" fill="var(--teal)"/><path d="M34 2v14h14z" fill="#4d8893"/><g stroke="#fff" stroke-width="4"><line x1="11" y1="30" x2="39" y2="30"/><line x1="11" y1="40" x2="39" y2="40"/><line x1="11" y1="50" x2="39" y2="50"/></g></svg>
    <h3>REASEARCH REPORT BY<br>HARBOURLINE UNIVERSITY</h3>
    <p style="top:160px">Nemo enim ipsam voluptatem quia voluptas sit aspernatur aut odit.</p>
    <span class="btn-red">DOWNLOAD</span>
  </div>
</section>

<section class="expedition">
  <h2 class="abs center">THE EXPEDITION</h2>
  <p class="abs lead" style="text-align:center">In May 2017 Mara Velden and Joss Arlen completed the first successful coasteering expedition of Hong Kong Island. In 6 days they climbed, swam, scrambled and hiked the entire coastline, took 51 water samples and mapped 163 trash pollution spots</p>
  <div class="abs video">
    <div role="img" aria-label="Video still of a green rocky headland meeting the sea" style="position:relative;width:100%;height:100%;background:linear-gradient(135deg,#8b98a2 0%,#4f6a4a 40%,#3d5536 60%,#6a6d66 100%)">
      <svg style="position:absolute;left:242px;top:137px" width="46" height="46" viewBox="0 0 46 46"><circle cx="23" cy="23" r="23" fill="#111" opacity=".75"/><path d="M18 14l13 9-13 9z" fill="#fff"/></svg>
    </div>
  </div>
  <a class="abs btn-outline" style="left:503px;top:582px;width:193px;height:52px;font-size:15px">GET MORE INFO</a>
  <div class="abs divider"></div>
  <h2 class="abs center sponsors-title">SPONSORS</h2>
  <div class="abs sponsor" style="left:97px"><span class="mark"></span>Northpass</div>
  <div class="abs sponsor" style="left:305px">Halvard</div>
  <div class="abs sponsor" style="left:512px"><span class="mark"></span>Clearwater</div>
  <div class="abs sponsor" style="left:719px">Harbourline</div>
  <div class="abs sponsor" style="left:924px"><span class="mark" style="border-radius:0"></span>Summitfold</div>
</section>

<footer class="footer">
  <div class="abs to-top">
    <svg width="66" height="24" viewBox="0 0 66 24"><path d="M33 0L66 24H0z" fill="#9a9a9a"/></svg>
    <div style="margin-top:6px">TO TOP</div>
  </div>
  <h4 class="abs" style="left:95px;top:150px">CONTACT FORM</h4>
  <div class="abs field" style="left:97px;top:217px;width:311px">Name :</div>
  <div class="abs field" style="left:416px;top:217px;width:309px">Phone no :</div>
  <div class="abs field" style="left:97px;top:261px;width:628px">Email :</div>
  <div class="abs field" style="left:97px;top:308px;width:628px;height:79px">Message :</div>
  <span class="abs btn-red" style="left:624px;top:406px;width:101px;height:35px">SUBMIT</span>

  <h4 class="abs" style="left:779px;top:150px">CONTACT INFORMATION</h4>
  <div class="abs info-row" style="top:202px"><span class="info-icon"><svg width="14" height="18" viewBox="0 0 14 18"><path d="M7 1a6 6 0 0 0-6 6c0 4.5 6 10 6 10s6-5.5 6-10a6 6 0 0 0-6-6z" fill="#fff"/><circle cx="7" cy="7" r="2.2" fill="#222"/></svg></span>27 Larchmont Terrace, Westhaven</div>
  <div class="abs info-row" style="top:260px"><span class="info-icon"><svg width="16" height="16" viewBox="0 0 16 16"><path d="M3 1l3 3-2 2c1 2 3 4 5 5l2-2 3 3-2 3C6 14 2 10 1 3z" fill="#fff"/></svg></span>1 555 014 2290</div>
  <div class="abs info-row" style="top:316px"><span class="info-icon"><svg width="16" height="12" viewBox="0 0 16 12"><rect width="16" height="12" rx="1" fill="#fff"/><path d="M0 1l8 6 8-6" stroke="#222" stroke-width="1.5" fill="none"/></svg></span>hello@tidemarkcircuit.org</div>
  <div class="abs" style="left:781px;top:380px;display:flex;gap:12px"><span class="social" style="background:#35508f"></span><span class="social" style="background:#a4763b"></span></div>

  <div class="abs foot-line"></div>
  <p class="abs center copyright">Copyright © 2017, Tidemark Circuit. All rights reserved.</p>
</footer>

</body>
</html>
```